Pel'k Marrowind Travel

We need a sleek, professional, inviting card to elicit global travel for the experienced and professional traveler. Royal blue, black and silver. (perhaps the wording could be silver with black shadow?-get creative) Maybe a watermark on the front and the full raised logo on the back.
We want a stylish and modern card, but professional.

```html
<!DOCTYPE html>
<html lang="en">
<head>
<meta charset="utf-8">
<title>Pel'k Marrowind Travel — Business Card</title>
<link href="https://fonts.googleapis.com/css2?family=Montserrat:wght@500;600;700&display=swap" rel="stylesheet">
<style>
  :root {
    --page-bg: #ffffff;
    --card-black: #000000;
    --card-white: #ffffff;
    --silver: #c6c6c6;
    --ink: #000000;
    --watermark: #eaf7fd;
    --shadow: rgba(0, 0, 0, 0.28);
  }
  * { margin: 0; padding: 0; box-sizing: border-box; }
  html, body {
    width: 1200px;
    height: 1000px;
    overflow: hidden;
    background: var(--page-bg);
    font-family: "Montserrat", sans-serif;
    color: var(--ink);
  }
  .sheet { position: relative; width: 1200px; height: 1000px; }
  .card {
    position: absolute;
    left: 245px;
    width: 714px;
    height: 408px;
    box-shadow: 3px 4px 8px var(--shadow);
    overflow: hidden;
  }
  .card--back { top: 71px; background: var(--card-black); }
  .card--front { top: 525px; background: var(--card-white); }

  .brand {
    position: absolute;
    left: 0; right: 0;
    top: 138px;
    display: flex;
    flex-direction: column;
    align-items: center;
    color: var(--silver);
    font-weight: 600;
    text-transform: uppercase;
    line-height: 1.1;
  }
  .brand__dot {
    width: 16px; height: 16px;
    border-radius: 50%;
    background: var(--silver);
    margin-bottom: 14px;
  }
  .brand__name { font-size: 30px; letter-spacing: 0.5px; }
  .brand__tag { font-size: 20px; letter-spacing: 6px; margin-top: 8px; }

  .watermark {
    position: absolute;
    left: 30px;
    top: 120px;
    color: var(--watermark);
    font-weight: 700;
    font-size: 90px;
    line-height: 1;
    letter-spacing: -1px;
    text-transform: uppercase;
    white-space: nowrap;
  }

  .person { position: absolute; left: 51px; top: 48px; }
  .person__name { font-weight: 700; font-size: 31px; line-height: 1.1; }
  .person__role { font-weight: 500; font-size: 19px; line-height: 1.2; }

  .contact {
    position: absolute;
    left: 51px;
    top: 283px;
    font-style: normal;
    font-weight: 500;
    font-size: 19px;
    line-height: 26px;
  }
  .address {
    position: absolute;
    right: 51px;
    top: 315px;
    text-align: right;
    font-style: normal;
    font-weight: 500;
    font-size: 19px;
    line-height: 22px;
  }

  .note {
    position: absolute;
    left: 974px;
    font-size: 16px;
    font-family: Arial, Helvetica, sans-serif;
    line-height: 21px;
    color: var(--ink);
  }
  .note--back { top: 453px; }
  .note--front { top: 895px; }
</style>
</head>
<body>
<main class="sheet">
  <section class="card card--back" aria-label="Card back">
    <div class="brand">
      <span class="brand__dot" aria-hidden="true"></span>
      <span class="brand__name">Pel'k Marrowind</span>
      <span class="brand__tag">Travel</span>
    </div>
  </section>
  <p class="note note--back">Silver Foil on Logo</p>

  <section class="card card--front" aria-label="Card front">
    <div class="watermark" aria-hidden="true">Pel'k<br>Marrowind</div>
    <div class="person">
      <h1 class="person__name">Sample Name</h1>
      <p class="person__role">Sample Position</p>
    </div>
    <address class="contact">
      123-456-7890<br>
      sampleemail@mailhub.net<br>
      www.samplewebsite.com
    </address>
    <address class="address">
      Sample Address, Unit #<br>
      City, 12345
    </address>
  </section>
  <p class="note note--front">Letterpress Black<br>on Text</p>
</main>
</body>
</html>
```